The Bright Meadow Foundation

This is a non profit . We are a 501(c)(3) charitable organization in the United States. The organization is a volunteer based group providing basic healthcare to those living in underserved rural areas around the world. I have attached a brochure that provides some information about the organization. We are looking for a basic 5 page web page Page 1 Photos that fade into the next x 3 with mission statementPage 2 About us - details about bright meadow foundation. also introducing our Founders of the organization. Marina Kellet, M.D. Dorla Penn , FNP, Rosa Tembley, FNP, Wade Marlow. ( will provide you info on each.Page 3 Projects coming up and futurePage 4 Get involved - Give a donation, Volunteer, Corporate supportPage 5 Support us and contact us with a message box.We mainly work in South America but anticipate trave to South Africa in the near future. Colors bright with emphasis on Reds and Purples. I have attached some photos and ideas. You can use or not use ok to use something similar if you so like

Target Market(s)

People interested in volunteering time or money to overseas medical work. NOT a religious base

Coding

Coded - Design and coding required

Number of Pages Required

1 page

Colors
876aae
ec1f27
f37022
9bcb3c

Requirements
Must have
• Colorful pictures nature, brings out emotion, colorful, children from various parts of the world, animals.
• Tried to down load some pictures but would not go thru.

```html
<!DOCTYPE html>
<html lang="en">
<head>
<meta charset="utf-8">
<title>The Bright Meadow Foundation</title>
<link href="https://fonts.googleapis.com/css2?family=Raleway:wght@400;500;600;700;800;900&family=Montserrat:wght@400;500;600;700&display=swap" rel="stylesheet">
<style>
:root{
  --purple:#876aae;
  --purple-light:#a58fcf;
  --orange:#f37022;
  --orange-deep:#ec5a14;
  --red:#ec1f27;
  --green:#9bcb3c;
  --green-deep:#6bb22a;
  --ink:#2b2b2b;
  --body:#7a7a7a;
  --grey-bg:#f4f4f4;
  --footer:#1a1a1a;
}
*{margin:0;padding:0;box-sizing:border-box}
html,body{width:1200px;height:4144px;overflow:hidden}
body{font-family:"Raleway",sans-serif;color:var(--ink);background:#fff;position:relative}
.btn{position:absolute;display:inline-flex;align-items:center;justify-content:center;background:var(--orange);color:#fff;font:700 11px "Montserrat",sans-serif;letter-spacing:.3px;border-radius:16px;height:30px;padding:0 18px;text-transform:uppercase;white-space:nowrap}

/* top bar */
.topbar{position:absolute;top:0;left:0;width:1200px;height:35px;background:var(--purple);color:#fff;font:400 11px "Montserrat",sans-serif}
.topbar .social{position:absolute;left:95px;top:8px;display:flex;gap:8px}
.topbar .social span{width:19px;height:19px;border-radius:50%;background:#fff;display:block}
.topbar .contact{position:absolute;right:92px;top:11px;display:flex;gap:26px}
.topbar .contact b{display:inline-block;width:9px;height:9px;border-radius:50%;background:var(--green);margin-right:6px;vertical-align:-1px}

/* header */
.header{position:absolute;top:35px;left:0;width:1200px;height:82px;background:#fff}
.brand{position:absolute;left:94px;top:30px;display:flex;align-items:center;gap:8px;font:600 17px "Raleway",sans-serif;color:var(--purple)}
.brand i{width:14px;height:14px;border-radius:50%;background:var(--purple);display:block}
.nav{position:absolute;right:92px;top:33px;display:flex;gap:55px;font:600 12px "Raleway",sans-serif;font-variant:small-caps;letter-spacing:.5px;color:#333}
.nav .active{color:var(--purple);position:relative}
.nav .active:after{content:"";position:absolute;left:50%;top:18px;width:10px;height:8px;margin-left:-5px;border-bottom:3px solid var(--green);border-radius:0 0 8px 8px}

/* hero */
.hero{position:absolute;top:117px;left:0;width:1200px;height:483px;background:radial-gradient(ellipse at 70% 45%,#cbbfae 0%,#8d7f6e 40%,#3f3830 100%)}
.hero-title{position:absolute;left:93px;top:140px;height:86px;padding:0 17px;background:rgba(40,36,30,.9);display:flex;align-items:center;font:900 36px "Raleway",sans-serif;color:#fff;letter-spacing:.3px}
.hero-title em{font-style:normal;color:var(--orange);margin-left:10px}
.hero-sub{position:absolute;left:93px;top:236px;height:41px;padding:0 12px;background:rgba(107,110,50,.85);display:flex;align-items:center;font:700 21px "Raleway",sans-serif;color:#fff}
.hero .btn{left:93px;top:286px}

/* section title */
.sec-title{position:absolute;left:0;width:1200px;text-align:center;font:800 36px "Raleway",sans-serif;color:var(--ink)}
.sec-lead{position:absolute;left:0;width:1200px;text-align:center;font:400 12.5px/21px "Montserrat",sans-serif;color:var(--body)}

/* get involved */
.involve{position:absolute;top:791px;width:327px;height:208px;display:flex;align-items:center;justify-content:center;font:700 21px "Raleway",sans-serif;color:#fff}
.involve.donate{left:93px;background:linear-gradient(135deg,var(--purple-light),var(--purple))}
.involve.volunteer{left:437px;background:linear-gradient(135deg,#f79a3a,var(--orange-deep))}
.involve.corporate{left:780px;background:linear-gradient(135deg,var(--green),var(--green-deep))}

/* about */
.about-bg{position:absolute;left:0;top:1045px;width:1107px;height:540px;background:var(--grey-bg)}
.about-photo{position:absolute;left:640px;top:1047px;width:451px;height:444px;background:linear-gradient(160deg,#c5362f 0%,#8b4c8a 45%,#d68a3a 100%)}
.about-kicker{position:absolute;left:94px;top:1124px;font:400 22px "Raleway",sans-serif;color:#333}
.about-head{position:absolute;left:94px;top:1150px;font:800 37px "Raleway",sans-serif;color:#333}
.about-head em{font-style:normal;color:var(--purple)}
.about-text{position:absolute;left:94px;top:1212px;width:510px;font:400 12px/21px "Montserrat",sans-serif;color:var(--body)}
.about .btn{left:94px;top:1379px}

/* founders */
.founders-band{position:absolute;left:0;top:1585px;width:855px;height:57px}
.founders-title{position:absolute;left:448px;top:1593px;font:800 35px "Raleway",sans-serif;color:#fff}
.founders-grey{position:absolute;left:0;top:1642px;width:93px;height:171px;background:var(--grey-bg)}
.founder{position:absolute;top:1687px;width:242px}
.founder .photo{width:242px;height:227px}
.founder h3{margin-top:24px;font:500 16px "Raleway",sans-serif;color:#333}
.founder .role{font:400 9px "Montserrat",sans-serif;color:#888;margin-top:3px}
.founder p{margin-top:16px;font:400 10px/16px "Montserrat",sans-serif;color:#888;width:215px;height:50px}
.founder .btn{position:relative;margin-top:21px}

/* projects */
.projects{position:absolute;left:0;top:2159px;width:1200px;height:297px;background:linear-gradient(180deg,#262626,#151515)}
.projects h2{position:absolute;left:0;top:122px;width:1200px;text-align:center;font:800 36px "Raleway",sans-serif;color:#fff}
.projects p{position:absolute;left:170px;top:176px;width:860px;text-align:center;font:400 12px/21px "Montserrat",sans-serif;color:#ddd}
.tile{position:absolute;width:300px;height:246px}
.tile-label{position:absolute;inset:0;background:rgba(236,31,39,.85);display:flex;align-items:center;justify-content:center;font:700 16px "Raleway",sans-serif;color:#fff}

/* contact */
.card{position:absolute;left:93px;top:3145px;width:1014px;height:526px;background:#fff;box-shadow:0 4px 26px rgba(0,0,0,.1)}
.card .photo{position:absolute;left:0;top:0;width:509px;height:526px;background:linear-gradient(150deg,#5d7a2c 0%,#a7b34c 35%,#c9312a 60%,#3d5a9a 85%)}
.card h2{position:absolute;left:543px;top:38px;font:800 33px "Raleway",sans-serif;color:#333}
.field{position:absolute;height:30px;border:1px solid #dcdcdc;font:400 10px "Montserrat",sans-serif;color:#555;display:flex;align-items:center}
.field i{width:24px;height:28px;background:var(--green);margin-right:8px;flex:none}
.field.msg{align-items:flex-start;height:107px}
.card .btn{left:872px;top:338px;width:103px}
.info-icon{position:absolute;left:543px}
.info-label{position:absolute;font:400 10px "Montserrat",sans-serif;color:#666}
.info-value{position:absolute;font:700 14px "Montserrat",sans-serif;color:#333;letter-spacing:.5px}
.soc{position:absolute;left:842px;display:flex;align-items:center;gap:10px;font:400 10px "Montserrat",sans-serif;color:#555}
.soc span{width:30px;height:30px;border-radius:50%;display:block}

/* footer */
.footer{position:absolute;left:0;top:3761px;width:1200px;height:383px;background:var(--footer);color:#cfcfcf}
.footer h4{position:absolute;top:70px;font:500 17px "Raleway",sans-serif;color:#fff;padding-bottom:8px;border-bottom:2px solid var(--orange)}
.footer .col{position:absolute;top:115px;font:400 12px/27px "Montserrat",sans-serif;color:#cfcfcf}
.footer .org{line-height:20px;width:240px}
.hl{color:var(--green)}
.news{position:absolute;left:840px;display:flex;gap:12px}
.news .thumb{width:56px;height:44px;background:linear-gradient(135deg,#a45b38,#d9b26a);flex:none}
.news b{display:block;font:400 14px "Raleway",sans-serif;color:#fff}
.news small{display:block;font:400 8px/12px "Montserrat",sans-serif;color:#999;width:200px}
.copy{position:absolute;left:96px;top:283px;font:400 12px/20px "Montserrat",sans-serif;color:#bbb}
.foot-brand{position:absolute;left:530px;top:290px;display:flex;align-items:center;gap:8px;font:600 15px "Raleway",sans-serif;color:#fff}
.foot-brand i{width:12px;height:12px;border-radius:50%;background:#fff;display:block}
</style>
</head>
<body>

<div class="topbar">
  <div class="social"><span></span><span></span></div>
  <div class="contact">
    <div><b></b>Call Us: 1-555-014-2290</div>
    <div><b></b>Mail Us: info@brightmeadowfoundation.org</div>
  </div>
</div>

<header class="header">
  <div class="brand"><i></i>Bright Meadow</div>
  <nav class="nav">
    <span class="active">Home</span><span>About Us</span><span>Projects</span><span>Get Involved</span><span>Contact Us</span>
  </nav>
</header>

<section class="hero" role="img" aria-label="Sepia portrait photograph of a smiling child">
  <div class="hero-title">SAVE OUR BELOVED <em>EARTH</em></div>
  <div class="hero-sub">YOUR DONATION CAN SAVE MANY LIVES</div>
  <span class="btn">Donate Now</span>
</section>

<h2 class="sec-title" style="top:663px">GET INVOLVED</h2>
<p class="sec-lead" style="top:717px">If you use this site regularly and would like to help keep the site on the Internet, please consider donating a small<br>sumto help pay for the hosting and bandwidth bill.</p>

<div class="involve donate">GIVE A DONATION</div>
<div class="involve volunteer">VOLUNTEER</div>
<div class="involve corporate">CORPORATE SUPPORT</div>

<section class="about">
  <div class="about-bg"></div>
  <div class="about-kicker">ABOUT THE BRIGHT</div>
  <div class="about-head">MEADOW <em>FOUNDATION</em></div>
  <p class="about-text">The Bright Meadow Foundation was founded with the aim of helping rural and indigenous individuals in various parts of the world. The Foundation's vision is to see that every woman, man and child have access to basic medical care and treatment as well as fundamental knowledge in preventative care. There are many people living in regions of the world today who have limited or no access to health centers. Often, these individuals travel hours and in many instances days for basic care that often times can be averted with preventative care measures.</p>
  <span class="btn">Read More</span>
  <div class="about-photo" role="img" aria-label="Photograph of a woman in colourful traditional Andean dress holding a small child"></div>
</section>

<section class="founders">
  <svg class="founders-band" viewBox="0 0 855 57" preserveAspectRatio="none"><polygon points="0,0 855,0 825,57 0,57" fill="var(--green)"/></svg>
  <div class="founders-title">OUR FOUNDERS</div>
  <div class="founders-grey"></div>

  <div class="founder" style="left:93px">
    <div class="photo" role="img" aria-label="Portrait photograph of Dorla Penn" style="background:linear-gradient(135deg,#c23a2e,#3b57b4)"></div>
    <h3>DORLA PENN, FNP</h3><div class="role">( CO-FOUNDER )</div>
    <p>Dorla Penn is a Nurse Practitioner who is currently practicing in her home state of Colorado.</p>
    <span class="btn">Read More</span>
  </div>
  <div class="founder" style="left:351px">
    <div class="photo" role="img" aria-label="Portrait photograph of Wade Marlow" style="background:linear-gradient(135deg,#7a3fd6,#d05bc4)"></div>
    <h3>WADE MARLOW</h3><div class="role">( CO-FOUNDER )</div>
    <p>Wade Marlow is a stylist and make-up artist in Boulder ,Colorado. He has always had a passion for...</p>
    <span class="btn">Read More</span>
  </div>
  <div class="founder" style="left:608px">
    <div class="photo" role="img" aria-label="Portrait photograph of Rosa Tembley" style="background:linear-gradient(135deg,#6e8a4a,#d8b89a)"></div>
    <h3>ROSA TEMBLEY, FNP</h3><div class="role">( CO-FOUNDER )</div>
    <p>Rosa is committed to live her life in service to others and make a global difference in the world.</p>
    <span class="btn">Read More</span>
  </div>
  <div class="founder" style="left:865px">
    <div class="photo" role="img" aria-label="Portrait photograph of Marina Kellet" style="background:linear-gradient(135deg,#8fa0a8,#5d6b4a)"></div>
    <h3>MARINA KELLET, M.D.</h3><div class="role">( CO-FOUNDER )</div>
    <p>Marina Kellet grew up just outside of San Francisco. She moved to Colorado in 2000 after completing...</p>
    <span class="btn">Read More</span>
  </div>
</section>

<section class="projects">
  <h2>PROJECTS</h2>
  <p>We are committed to investing in the health and welfare of our global community. The Foundation will continue to expand work into other rural areas of both Central and South America. In addition, We are currently working on a partnership with a nongovernmental organization in South Africa and hope to be expanding to this part of the globe in the near future.</p>
</section>

<div class="tile" style="left:0;top:2456px;background:linear-gradient(135deg,#7a2a1e,#c97a3a)" role="img" aria-label="Photograph of a woman wearing traditional jewellery"></div>
<div class="tile" style="left:300px;top:2456px;background:linear-gradient(135deg,#7a2c3a,#c65a4a)" role="img" aria-label="Project photograph"><div class="tile-label">FINIBUS BONORUM</div></div>
<div class="tile" style="left:600px;top:2456px;background:linear-gradient(135deg,#6a4e9a,#d0653a)" role="img" aria-label="Photograph of volunteers with local women and a child"></div>
<div class="tile" style="left:900px;top:2456px;background:linear-gradient(135deg,#c9a03a,#8a2e5a)" role="img" aria-label="Photograph of women in colourful dress seated in a courtyard"></div>
<div class="tile" style="left:0;top:2702px;background:linear-gradient(135deg,#5a4a3a,#c23a3a)" role="img" aria-label="Photograph of an elderly woman in a red sweater"></div>
<div class="tile" style="left:300px;top:2702px;background:linear-gradient(135deg,#3a2a2a,#b64a3a)" role="img" aria-label="Photograph of a child holding hands with a volunteer"></div>
<div class="tile" style="left:600px;top:2702px;background:linear-gradient(135deg,#8a5aa8,#3a3a4a)" role="img" aria-label="Photograph of a doctor examining a patient"></div>
<div class="tile" style="left:900px;top:2702px;background:linear-gradient(135deg,#b8652a,#5a6a8a)" role="img" aria-label="Photograph of a medical check-up in a village clinic"></div>

<h2 class="sec-title" style="top:3011px">SUPPORT US</h2>
<p class="sec-lead" style="top:3069px">Your donations allow us to provide medical care, health resources and supplies, and wellness education to the communities we serve.<br>The links below are some of the ways you can donate to our organization.</p>

<section class="card">
  <div class="photo" role="img" aria-label="Photograph of a red macaw perched on a branch"></div>
  <h2>CONTACT US</h2>
  <div class="field" style="left:543px;top:95px;width:212px"><i></i>Name:</div>
  <div class="field" style="left:763px;top:95px;width:212px"><i></i>Email:</div>
  <div class="field" style="left:543px;top:134px;width:212px"><i></i>Phone:</div>
  <div class="field" style="left:763px;top:134px;width:212px"><i></i>Subjects:</div>
  <div class="field msg" style="left:543px;top:173px;width:432px"><i></i><span style="margin-top:9px">Message:</span></div>
  <span class="btn">Submit</span>
  <svg class="info-icon" style="top:398px" width="18" height="18" viewBox="0 0 18 18"><path d="M4 2 l3 0 l1.5 4 l-2 1.5 q1.5 3 4 4 l1.5 -2 l4 1.5 v3 q0 2 -2 2 q-12 -1 -13 -13 q0 -1 3 -1z" fill="none" stroke="var(--orange)" stroke-width="1.4"/></svg>
  <div class="info-label" style="left:543px;top:420px">Call Us:</div>
  <div class="info-value" style="left:543px;top:434px">1-555-014-2290</div>
  <svg class="info-icon" style="top:488px" width="20" height="15" viewBox="0 0 20 15"><rect x="1" y="1" width="18" height="13" fill="none" stroke="var(--orange)" stroke-width="1.4"/><path d="M1 1 l9 7 l9 -7" fill="none" stroke="var(--orange)" stroke-width="1.4"/></svg>
  <div class="info-label" style="left:543px;top:508px">Mail Us:</div>
  <div class="info-value" style="left:543px;top:522px;font-size:11px;letter-spacing:0">info@brightmeadowfoundation.org</div>
  <div class="info-label" style="left:842px;top:372px">Follow Us On Social</div>
  <div class="soc" style="top:395px"><span style="background:#3b5aa0"></span>Friendnet</div>
  <div class="soc" style="top:447px"><span style="background:#d8307a"></span>Snapgram</div>
</section>

<footer class="footer">
  <h4 style="left:94px">ORGANIZATION</h4>
  <div class="col org" style="left:94px">The Bright Meadow Foundation was founded with the aim of helping rural and indigenous individuals in various parts of the world. The Foundation's vision is to see that every woman, man and child have access... <span class="hl">Read More</span></div>
  <h4 style="left:414px">SITEMAP</h4>
  <div class="col" style="left:414px">Home<br>About Us<br>Get involved<br>Projects<br>Contact Us</div>
  <h4 style="left:621px">GET INVOLVED</h4>
  <div class="col" style="left:621px">Give a donation<br>Volunteer,<br>Corporate support</div>
  <h4 style="left:840px">NEWS</h4>
  <div class="news" style="top:118px"><div class="thumb" role="img" aria-label="News thumbnail photograph"></div><div><b>The standard Lorem Ipsum</b><small>Sed ut perspiciatis unde omnis iste natus error sit voluptatem... <span class="hl">Read More</span></small></div></div>
  <div class="news" style="top:186px"><div class="thumb" role="img" aria-label="News thumbnail photograph"></div><div><b>The standard Lorem Ipsum</b><small>Sed ut perspiciatis unde omnis iste natus error sit voluptatem... <span class="hl">Read More</span></small></div></div>
  <div class="news" style="top:254px"><div class="thumb" role="img" aria-label="News thumbnail photograph"></div><div><b>The standard Lorem Ipsum</b><small>Sed ut perspiciatis unde omnis iste natus error sit voluptatem... <span class="hl">Read More</span></small></div></div>
  <div class="copy">Copyright © 2019 <span class="hl">The Bright Meadow Foundation.</span><br>All rights reserved.</div>
  <div class="foot-brand"><i></i>Bright Meadow</div>
</footer>

</body>
</html>
```